family chiropractic health care team needs a modern business card design

Healthcare office with Chiropractors, Physiotherapists, Massage therapists and possibly other practitioners in the future. This is a friendly family office with patients of all ages (and lots of kids) that just moved into a new larger modern office.
Look at the website for photos of the office.
Design for the front and back of a business card required.
Text for the front:
Office logo and name of the office:
Bright Path Wellness Centre
Name of current Practitioner:
Dr. Marten Quovel B.Sc., D.C. Chiropractor
(But please include options to swap out name and title for other practitioners )

address:
218 Farrow Gate
Etobicoke ON.
K2J 6P4
Phone: 416-872-0196 (PATH)
Web site and email:
www.brightpathwellnesscentre.example
brightpathchiro@mailbox.example

2 versions of the back of the card:
1. text below
2. appointment schedule card

Text on back of card:
Chiropractic Card text on back of the card:
There is more to chiropractic than the relief of headaches and back pain! Our primary focus is the integrity of your nerve system, which controls and regulates every cell and tissue of your body. The moving bones of the spinal column can impair this vital communication link between your brain and body. We help improve the function and structure of your spine, reducing nerve system compromise. The result?
Even non-spinal related health problems can show improvement
without drugs
without surgery
regardless of age
for over a century
naturally

Appointment Card info For Back:
Please integrate design elements from the front of the card into an appointment card format.
M Tu W Th F Sat (and a line for writing on beside each one)

```html
<!DOCTYPE html>
<html lang="en">
<head>
<meta charset="utf-8">
<title>Bright Path Wellness Centre – Business Cards</title>
<link rel="stylesheet" href="https://fonts.googleapis.com/css2?family=Open+Sans:wght@400;600;700&family=Raleway:wght@700&family=Montserrat:wght@400&display=swap">
<style>
  :root {
    --bg: #9a9a9a;
    --card: #ffffff;
    --green: #99c255;
    --green-text: #8dc049;
    --grey-text: #7a7a7a;
    --ink: #222222;
    --band: #232323;
    --rule: #d9d9d9;
  }
  * { box-sizing: border-box; margin: 0; padding: 0; }
  html, body { width: 1200px; height: 1200px; overflow: hidden; }
  body {
    position: relative;
    background: var(--bg);
    font-family: "Open Sans", Arial, sans-serif;
  }
  .card {
    position: absolute;
    width: 610px;
    height: 356px;
    border-radius: 25px;
    overflow: hidden;
    box-shadow: 0 14px 30px rgba(0,0,0,0.28);
  }
  .brand {
    position: absolute;
    display: flex;
    align-items: center;
    gap: 12px;
    font-family: "Open Sans", Arial, sans-serif;
    font-weight: 700;
    line-height: 1.12;
  }
  .brand-dot { width: 18px; height: 18px; border-radius: 50%; flex: none; }

  /* Front */
  .card-front { left: 295px; top: 40px; background: var(--card); }
  .card-front .brand { left: 38px; top: 140px; font-size: 24px; color: var(--green-text); }
  .card-front .brand-dot { background: var(--green-text); }
  .divider { position: absolute; top: 20px; bottom: 20px; width: 1px; background: var(--rule); }
  .card-front .divider { left: 305px; }
  .contact { position: absolute; left: 330px; top: 84px; color: var(--grey-text); font-size: 16px; line-height: 21px; }
  .contact .person { font-family: "Raleway", Arial, sans-serif; font-weight: 700; color: var(--green-text); font-size: 17.5px; line-height: 21px; }
  .contact .title { font-weight: 700; font-size: 17px; margin-bottom: 21px; }
  .contact .office { font-weight: 700; }
  .contact .address { margin-bottom: 21px; }
  .contact-line { display: flex; align-items: center; gap: 7px; font-size: 15px; line-height: 24px; }
  .contact-line svg { width: 15px; height: 15px; flex: none; }

  /* Info back */
  .card-info { left: 291px; top: 421px; background: var(--green); color: #fff; }
  .card-info .divider { left: 306px; background: rgba(255,255,255,0.45); }
  .info-copy { position: absolute; left: 38px; top: 46px; width: 250px; font-size: 14.2px; line-height: 17px; }
  .info-copy p + p { margin-top: 17px; }
  .info-benefits { position: absolute; left: 333px; top: 46px; width: 250px; font-size: 14.2px; line-height: 17px; }
  .benefit-list { list-style: none; margin-top: 17px; }
  .benefit-list li { display: flex; align-items: center; gap: 3px; }
  .benefit-list svg { width: 11px; height: 11px; flex: none; }
  .card-info .brand { left: 333px; top: 224px; font-size: 24px; color: #fff; }
  .card-info .brand-dot { background: #fff; }

  /* Appointment back */
  .card-appointment { left: 291px; top: 808px; background: var(--card); }
  .appointment-rows { position: absolute; left: 40px; top: 58px; width: 510px; font-family: "Montserrat", Arial, sans-serif; color: var(--ink); font-size: 17px; }
  .when { display: flex; align-items: flex-end; height: 26px; }
  .when span { white-space: nowrap; }
  .write-line { display: block; height: 1px; background: var(--ink); width: 199px; margin: 0 10px 5px 8px; }
  .days { display: flex; justify-content: space-between; margin: 13px 0 27px; }
  .day { display: flex; align-items: center; gap: 5px; }
  .box { width: 21px; height: 21px; border: 1.3px solid #444; }
  .contact-band { position: absolute; left: 0; right: 0; bottom: 0; height: 110px; background: var(--band); }
  .contact-band .brand { left: 30px; top: 30px; font-size: 20px; color: var(--green-text); }
  .contact-band .brand-dot { background: var(--green-text); width: 15px; height: 15px; }
  .band-contact { position: absolute; right: 31px; top: 22px; text-align: right; color: #b5b5b5; font-size: 14.5px; line-height: 19px; }
  .band-contact .phone { color: var(--green-text); font-weight: 700; }
</style>
</head>
<body>

<section class="card card-front" aria-label="Business card front">
  <div class="brand"><span class="brand-dot"></span><span>Bright Path<br>Wellness Centre</span></div>
  <div class="divider"></div>
  <div class="contact">
    <div class="person">Name Surname</div>
    <div class="title">Title</div>
    <div class="office">Bright Path Wellness Centre</div>
    <div class="address">218 Farrow Gate<br>Etobicoke, ON K2J 6P4</div>
    <div class="contact-line">
      <svg viewBox="0 0 24 24"><path fill="#8dc049" d="M6.6 10.8a15.1 15.1 0 0 0 6.6 6.6l2.2-2.2c.3-.3.7-.4 1-.2 1.1.4 2.3.6 3.6.6.6 0 1 .4 1 1V20c0 .6-.4 1-1 1A17 17 0 0 1 3 4c0-.6.4-1 1-1h3.5c.6 0 1 .4 1 1 0 1.3.2 2.5.6 3.6.1.3 0 .7-.2 1l-2.3 2.2z"/></svg>
      <span>416-872-0196 (PATH)</span>
    </div>
    <div class="contact-line">
      <svg viewBox="0 0 24 24"><rect x="2" y="5" width="20" height="14" fill="#8dc049"/><path d="M2 5l10 8 10-8" fill="none" stroke="#fff" stroke-width="1.8"/></svg>
      <span>brightpathchiro@mailbox.example</span>
    </div>
    <div class="contact-line">
      <svg viewBox="0 0 24 24"><g fill="none" stroke="#8dc049" stroke-width="2"><circle cx="12" cy="12" r="9.5"/><ellipse cx="12" cy="12" rx="4" ry="9.5"/><path d="M2.5 12h19M4 7h16M4 17h16"/></g></svg>
      <span>brightpathwellnesscentre.example</span>
    </div>
  </div>
</section>

<section class="card card-info" aria-label="Business card back with chiropractic information">
  <div class="info-copy">
    <p>There is more to chiropractic than the relief of headaches and back pain!</p>
    <p>Our primary focus is the integrity of your nerve system, which controls and regulates every cell and tissue of your body. The moving bones of the spinal column can impair this vital communication link between your brain and body. We help improve the function and structure of your spine, reducing nerve system compromise. The result?</p>
  </div>
  <div class="divider"></div>
  <div class="info-benefits">
    <p>Even non-spinal related health problems can show improvement</p>
    <ul class="benefit-list">
      <li><svg viewBox="0 0 12 12"><path d="M1.5 6.5l3 3 6-7" fill="none" stroke="#fff" stroke-width="1.8"/></svg>without drugs</li>
      <li><svg viewBox="0 0 12 12"><path d="M1.5 6.5l3 3 6-7" fill="none" stroke="#fff" stroke-width="1.8"/></svg>without surgery</li>
      <li><svg viewBox="0 0 12 12"><path d="M1.5 6.5l3 3 6-7" fill="none" stroke="#fff" stroke-width="1.8"/></svg>regardless of age</li>
      <li><svg viewBox="0 0 12 12"><path d="M1.5 6.5l3 3 6-7" fill="none" stroke="#fff" stroke-width="1.8"/></svg>for over a century</li>
      <li><svg viewBox="0 0 12 12"><path d="M1.5 6.5l3 3 6-7" fill="none" stroke="#fff" stroke-width="1.8"/></svg>naturally</li>
    </ul>
  </div>
  <div class="brand"><span class="brand-dot"></span><span>Bright Path<br>Wellness Centre</span></div>
</section>

<section class="card card-appointment" aria-label="Appointment card back">
  <div class="appointment-rows">
    <div class="when"><span>Date:</span><i class="write-line"></i><span>Time:</span><i class="write-line"></i></div>
    <div class="days">
      <span class="day"><i class="box"></i>Mon</span>
      <span class="day"><i class="box"></i>Tue</span>
      <span class="day"><i class="box"></i>Wed</span>
      <span class="day"><i class="box"></i>Thu</span>
      <span class="day"><i class="box"></i>Fri</span>
      <span class="day"><i class="box"></i>Sat</span>
      <span class="day"><i class="box"></i>Sun</span>
    </div>
    <div class="when"><span>Date:</span><i class="write-line"></i><span>Time:</span><i class="write-line"></i></div>
    <div class="days">
      <span class="day"><i class="box"></i>Mon</span>
      <span class="day"><i class="box"></i>Tue</span>
      <span class="day"><i class="box"></i>Wed</span>
      <span class="day"><i class="box"></i>Thu</span>
      <span class="day"><i class="box"></i>Fri</span>
      <span class="day"><i class="box"></i>Sat</span>
      <span class="day"><i class="box"></i>Sun</span>
    </div>
  </div>
  <div class="contact-band">
    <div class="brand"><span class="brand-dot"></span><span>Bright Path<br>Wellness Centre</span></div>
    <div class="band-contact">
      <div class="phone">416-872-0196 (PATH)</div>
      <div>brightpathchiro@mailbox.example</div>
      <div>brightpathwellnesscentre.example</div>
    </div>
  </div>
</section>

</body>
</html>
```